Mirvane Trinkets
Lucinda Harrow Designs
Mirvane Trinkets -
Creative Brief
Simple
Lucinda Harrow
Jewelry Designer
2719 Quillfern Ln Dallas TX 75294
lucinda@mirvane-example.com
www.mirvane-example.com
Please do a few designs!
Maybe just the logo?

```html
<!DOCTYPE html>
<html lang="en">
<head>
<meta charset="utf-8">
<title>Mirvane Trinkets – Business Card</title>
<link rel="stylesheet" href="https://fonts.googleapis.com/css2?family=Arimo:wght@400;700&display=swap">
<style>
  :root {
    --page: #ffffff;
    --card-edge: #3a3a3a;
    --ink: #111111;
    --brand: #2f5f5a;
    --silver-light: #f4f4f4;
    --silver-mid: #d4d4d4;
    --silver-dark: #a9a9a9;
    --mark: #b8b8b8;
  }
  * { box-sizing: border-box; margin: 0; padding: 0; }
  html, body {
    width: 1200px; height: 857px; overflow: hidden;
    background: var(--page);
    font-family: "Arimo", Arial, sans-serif;
    color: var(--ink);
  }
  .canvas { position: relative; width: 1200px; height: 857px; }

  .card {
    position: absolute;
    border: 2px solid var(--card-edge);
    overflow: hidden;
  }
  .card--front { left: 5px; top: 5px; width: 948px; height: 408px; background: var(--page); }
  .card--back {
    left: 475px; top: 439px; width: 718px; height: 413px;
    background: linear-gradient(125deg, var(--silver-mid) 0%, var(--silver-light) 38%, var(--silver-mid) 60%, var(--silver-light) 80%, var(--silver-dark) 100%);
  }

  .brand {
    position: absolute; left: 0; right: 0;
    display: flex; flex-direction: column; align-items: center;
  }
  .brand__dot {
    border-radius: 50%;
    background: radial-gradient(circle at 35% 35%, var(--silver-light), var(--mark) 70%);
  }
  .brand__name {
    font-weight: 400; color: var(--brand); letter-spacing: 1px; white-space: nowrap;
  }
  .card--front .brand { top: 36px; }
  .card--front .brand__dot { width: 84px; height: 84px; margin-bottom: 18px; }
  .card--front .brand__name { font-size: 40px; }

  .card--back .brand { top: 60px; }
  .card--back .brand__dot { width: 120px; height: 120px; margin-bottom: 40px; }
  .card--back .brand__name { font-size: 50px; }

  .nameband {
    position: absolute; left: 0; right: 0; top: 232px; height: 60px;
    background: linear-gradient(90deg, var(--silver-light) 0%, var(--silver-mid) 30%, var(--silver-mid) 70%, var(--silver-light) 100%);
    display: flex; align-items: center;
    padding-left: 240px;
    font-size: 19px;
  }
  .nameband__name { font-weight: 700; }
  .nameband__role { font-weight: 400; }

  .contact {
    position: absolute; left: 0; width: 792px; top: 322px;
    text-align: center; font-size: 17px; line-height: 22px;
  }
  .contact__label { font-weight: 700; }

  .website {
    position: absolute; left: 0; right: 0; bottom: 20px;
    text-align: center; font-size: 17px; font-weight: 700;
  }
</style>
</head>
<body>
<main class="canvas">
  <section class="card card--front">
    <div class="brand">
      <span class="brand__dot" aria-hidden="true"></span>
      <span class="brand__name">Mirvane Trinkets</span>
    </div>
    <div class="nameband">
      <span class="nameband__name">Lucinda Harrow</span>&nbsp;<span class="nameband__role">| Jewelry Designer</span>
    </div>
    <address class="contact" style="font-style:normal">
      <div><span class="contact__label">P:</span> 214-555-0187</div>
      <div><span class="contact__label">E:</span> lucinda@mirvane-example.com</div>
      <div><span class="contact__label">A:</span> 2719 Quillfern Ln Dallas TX 75294</div>
    </address>
  </section>

  <section class="card card--back">
    <div class="brand">
      <span class="brand__dot" aria-hidden="true"></span>
      <span class="brand__name">Mirvane Trinkets</span>
    </div>
    <div class="website">www.mirvane-example.com</div>
  </section>
</main>
</body>
</html>
```